Veltrano - Mechanic/Collision Center Business Card

We're looking for a business card design for our mechanic/ collision repair shop.

Can be with colours or monochromatic.

See the attached files.

Many thanks

```html
<!DOCTYPE html>
<html lang="en">
<head>
<meta charset="utf-8">
<title>Veltrano Business Card</title>
<link rel="stylesheet" href="https://fonts.googleapis.com/css2?family=Lato:wght@400;700;900&display=swap">
<style>
  :root {
    --stage: #3b3b3b;
    --card: #1f2022;
    --accent: #2a9bdc;
    --text: #e6e6e6;
    --muted: #bdbdbd;
    --logo-text: #ffffff;
  }
  * { margin: 0; padding: 0; box-sizing: border-box; }
  html, body {
    width: 1200px; height: 900px; overflow: hidden;
    background: var(--stage);
    font-family: "Lato", sans-serif;
  }
  .stage {
    position: relative; width: 1200px; height: 900px;
  }
  .card {
    position: absolute;
    width: 560px; height: 320px;
    background: var(--card);
    box-shadow: 0 14px 30px rgba(0,0,0,0.45);
    overflow: hidden;
  }
  .card::after {
    content: ""; position: absolute; left: 0; right: 0; bottom: 0;
    height: 9px; background: var(--accent);
  }
  .card--front { left: 320px; top: 100px; }
  .card--back  { left: 320px; top: 480px; }

  .brand {
    display: flex; align-items: center; gap: 12px;
    color: var(--logo-text);
    font-weight: 900; letter-spacing: 1px;
    text-transform: uppercase;
  }
  .brand__dot {
    background: var(--accent); border-radius: 50%;
  }
  .card--front .brand {
    position: absolute; left: 0; right: 0; top: 112px;
    justify-content: center; font-size: 50px;
  }
  .card--front .brand__dot { width: 30px; height: 30px; }
  .card--front .web {
    position: absolute; left: 0; right: 0; top: 196px;
    text-align: center; color: var(--text);
    font-size: 15px; letter-spacing: 1px;
  }

  .card--back .brand {
    position: absolute; left: 34px; top: 96px; width: 220px;
    font-size: 32px; gap: 10px;
  }
  .card--back .brand__dot { width: 20px; height: 20px; }
  .divider {
    position: absolute; left: 268px; top: 60px;
    width: 1px; height: 190px; background: var(--accent);
  }
  .contact {
    position: absolute; left: 296px; top: 46px;
    color: var(--text); font-size: 15px; line-height: 1.45;
  }
  .contact__name {
    color: var(--accent); font-size: 25px; font-weight: 400; line-height: 1.2;
  }
  .contact__role { color: var(--muted); font-size: 15px; margin-bottom: 8px; }
  .contact__address { margin-bottom: 6px; }
  .contact__row { display: flex; align-items: center; gap: 10px; }
  .contact__row svg { width: 13px; height: 13px; flex: none; fill: var(--accent); }
</style>
</head>
<body>
<main class="stage">

  <section class="card card--front">
    <div class="brand"><span class="brand__dot"></span><span>Veltrano</span></div>
    <p class="web">www.veltrano.com</p>
  </section>

  <section class="card card--back">
    <div class="brand"><span class="brand__dot"></span><span>Veltrano</span></div>
    <div class="divider"></div>
    <div class="contact">
      <h1 class="contact__name">Daniel Hartwell</h1>
      <p class="contact__role">Manager</p>
      <p class="contact__address">418 Birch Hollow Road<br>Austin, TX 78745</p>
      <p class="contact__row">
        <svg viewBox="0 0 16 16" aria-hidden="true"><path d="M3 1l3 3-1.5 2a9 9 0 005.5 5.5L12 10l3 3-2 2C7 15 1 9 1 3z"/></svg>
        555 010 4820
      </p>
      <p class="contact__row">
        <svg viewBox="0 0 16 16" aria-hidden="true"><rect x="4" y="1" width="8" height="4"/><rect x="1" y="6" width="14" height="6" rx="1"/><rect x="4" y="10" width="8" height="5"/></svg>
        555 010 4821
      </p>
      <p class="contact__row">
        <svg viewBox="0 0 16 16" aria-hidden="true"><path d="M1 3h14v10H1z M1 3l7 6 7-6" stroke="#1f2022" stroke-width="1"/></svg>
        info@veltrano.com
      </p>
      <p class="contact__row">
        <svg viewBox="0 0 16 16" aria-hidden="true"><circle cx="8" cy="8" r="7"/><path d="M1 8h14M8 1c-3 4-3 10 0 14M8 1c3 4 3 10 0 14" stroke="#1f2022" stroke-width="1" fill="none"/></svg>
        www.veltrano.com
      </p>
    </div>
  </section>

</main>
</body>
</html>
```